Business card for Eyelash extension salon in Beverly Hills,California USA

We need new business card for our salon in Beverly Hills. The salon name is 'Lumarra' . We would like to have...Business name: Lumarra Name of person: will provide later Address 6128 N.Corbel Ridge Blvd Beverly Hills , CA 90210 Phone: will provide later (Text only) Web: www.lumarrastudio-example.com Pictogrid icon, Friendvale icon follow us for seasonal campaign and news @lumarrastudioexample Design should look elegant, high-end, clean, simple, cohesive with my brand. Please refer my brand board. Business name color will be metallic bronzy color. Im thinking grey background or white background. Thanks

Target Market(s)

25-35. Gender neutral. People who are in Entertainment business industry.
This is High-end Eyelash extension salon in Beverly Hills

Industry/Entity Type

Beauty Salon

Contact Information for Business Card

Business name: Lumarra
Name of person: will provide later
Address 6128 N.Corbel Ridge Blvd Beverly Hills , CA 90210
Phone: will provide later (Text only)
Web: www.lumarrastudio-example.com
Pictogrid icon, Friendvale icon
follow us for seasonal campaign and news @lumarrastudioexample

Requirements
Must have
• Beautiful, elegant, clean and simple look but very attractive and modern
Should not have
• We don't like too clutter, too busy designs.

```html
<!DOCTYPE html>
<html lang="en">
<head>
<meta charset="utf-8">
<title>Lumarra Beverly Hills – Business Card</title>
<link rel="stylesheet" href="https://fonts.googleapis.com/css2?family=Cormorant+Garamond:wght@400;500&family=Josefin+Sans:wght@300;400&display=swap">
<style>
  :root {
    --page: #ece6dc;
    --bronze: #a2806a;
    --bronze-deep: #8f6d57;
    --bronze-light: #b8977f;
    --ink-light: #ffffff;
    --marble-1: #f6f6f5;
    --marble-2: #e4e4e3;
    --marble-3: #d3d3d2;
    --serif: "Cormorant Garamond", "Times New Roman", serif;
    --sans: "Josefin Sans", "Helvetica Neue", sans-serif;
  }
  * { box-sizing: border-box; margin: 0; padding: 0; }
  html, body { width: 1200px; height: 800px; overflow: hidden; }
  body {
    background: var(--page);
    display: flex;
    align-items: center;
    justify-content: center;
    gap: 60px;
  }
  .card {
    position: relative;
    width: 520px;
    height: 297px;
    overflow: hidden;
    box-shadow: 0 10px 24px rgba(80, 60, 40, 0.18);
  }

  /* Front */
  .card--front { background: var(--bronze); color: var(--ink-light); }
  .front__photo {
    position: absolute; inset: 0;
    background:
      radial-gradient(ellipse 40% 30% at 70% 30%, var(--bronze-deep) 0%, transparent 70%),
      radial-gradient(ellipse 35% 25% at 22% 52%, var(--bronze-deep) 0%, transparent 70%),
      linear-gradient(160deg, var(--bronze-light) 0%, var(--bronze) 55%, var(--bronze-deep) 100%);
  }
  .front__brand {
    position: absolute;
    left: 0; right: 0; top: 72px;
    text-align: center;
  }
  .brand-name {
    font-family: var(--serif);
    font-weight: 400;
    font-size: 78px;
    line-height: 1;
    letter-spacing: 2px;
  }
  .brand-city {
    margin-top: 8px;
    padding-left: 150px;
    font-family: var(--sans);
    font-weight: 300;
    font-size: 10px;
    letter-spacing: 3px;
  }
  .front__web {
    position: absolute;
    left: 0; right: 0; bottom: 44px;
    text-align: center;
    font-family: var(--serif);
    font-size: 17px;
    letter-spacing: 0.5px;
  }

  /* Back */
  .card--back { color: var(--bronze); }
  .back__marble {
    position: absolute; inset: 0;
    background:
      linear-gradient(125deg, transparent 40%, var(--marble-3) 48%, transparent 56%),
      linear-gradient(200deg, transparent 60%, var(--marble-2) 70%, transparent 80%),
      linear-gradient(160deg, var(--marble-1) 0%, var(--marble-2) 100%);
  }
  .back__frame {
    position: absolute;
    inset: 14px;
    border: 1px solid var(--bronze);
  }
  .back__person {
    position: absolute;
    left: 58px; top: 100px;
    font-family: var(--sans);
    font-weight: 400;
    font-size: 17px;
    letter-spacing: 0.5px;
  }
  .back__rule {
    position: absolute;
    left: 240px; top: 86px;
    width: 1px; height: 118px;
    background: var(--bronze);
  }
  .back__rule-short {
    position: absolute;
    left: 240px; top: 146px;
    width: 70px; height: 1px;
    background: var(--bronze);
    transform: translateX(-70px);
  }
  .back__address {
    position: absolute;
    left: 258px; top: 84px;
    font-family: var(--serif);
    font-size: 17px;
    line-height: 1.32;
    font-style: normal;
  }
  .back__social {
    position: absolute;
    left: 258px; top: 190px;
    display: flex; gap: 14px;
    font-family: var(--serif);
    font-size: 12px;
  }
  .social { display: flex; align-items: center; gap: 5px; }
  .social__dot {
    width: 9px; height: 9px;
    border-radius: 50%;
    background: var(--bronze);
  }
  .back__follow {
    position: absolute;
    left: 0; right: 0; bottom: 26px;
    text-align: center;
    font-family: var(--serif);
    font-size: 15px;
  }
</style>
</head>
<body>
  <section class="card card--front" aria-label="Business card front">
    <div class="front__photo" role="img" aria-label="Soft-focus close-up photo of closed eyes with lash extensions, toned in bronze"></div>
    <div class="front__brand">
      <div class="brand-name">Lumarra</div>
      <div class="brand-city">BEVERLY HILLS</div>
    </div>
    <div class="front__web">www.lumarrastudio-example.com</div>
  </section>

  <section class="card card--back" aria-label="Business card back">
    <div class="back__marble" role="img" aria-label="White and grey marble texture"></div>
    <div class="back__frame"></div>
    <div class="back__person">NAME OF PERSON</div>
    <div class="back__rule"></div>
    <div class="back__rule-short"></div>
    <address class="back__address">
      6128 N.Corbel Ridge Blvd<br>
      Beverly Hills<br>
      CA 90210<br>
      Phone (Text only)
    </address>
    <div class="back__social">
      <span class="social"><span class="social__dot"></span>Friendvale</span>
      <span class="social"><span class="social__dot"></span>Pictogrid</span>
    </div>
    <div class="back__follow">follow us for seasonal campaign and news @lumarrastudioexample</div>
  </section>
</body>
</html>
```